"Copper Horizons" poster for feature film

I need a poster for my first narrative feature film. Genre: Drama/Comedy. Synopsis: After going through a break up and moving back home, Tobias struggles through a "quarter life crisis" in pursuit of his dream of making a feature film. Tobias wants to tell a compassionate story about mental illness and its effects on a family, but the lines between fiction and reality are blurred, challenging the bond between two brothers.

Target Market(s)

Film Festivals, Prospective viewers on Vidorly/Quorvia.

Industry/Entity Type

Film Production

Other font styles liked:
• Birch STD

Colors
faa54b
f78f20
85abd2
3176b5
0355a3
fac994
f9ba93
f37122
fece3e

Requirements
Must have
• Title: Copper Horizons
• Minimalist approach.
• Please look at reference posters/prototypes.
Nice to have
• -the idea of contrasting the two brothers and the struggle of living with a mental illness.
• -the setting of the film is in Arizona, desert, living back at home as an adult.
• -the struggle of a writer. A film about a film.
• 5 phases of "The Quarter Life Crisis"
• 1. You feel trapped by your life choices, like your job, relationship, or both. You’re living on “autopilot.”
• 2. You get a sense of “I’ve got to get out of this” and feel a growing sense that change is possible if you just take a leap.
• 3. You quit the job, end the relationship, or break the commitment that’s making you feel trapped. Then you detach and enter a “time out” period where try to rediscover who you are and who you want to be.
• 4. You begin rebuilding your life slowly but surely.
• 5. You develop new commitments that are more in line with your interests and aspirations.

```html
<!DOCTYPE html>
<html lang="en">
<head>
<meta charset="utf-8">
<title>Copper Horizons — Poster</title>
<link rel="stylesheet" href="https://fonts.googleapis.com/css2?family=Michroma&family=Pathway+Gothic+One&display=swap">
<style>
  :root {
    --paper: #ecebe6;
    --mustard: #f1c232;
    --bone: #f3f1ea;
    --copper: #e0681f;
    --umber: #4b3c17;
    --rust: #d45f1c;
    --credit-ink: #8b6a1c;
  }
  html, body {
    margin: 0;
    padding: 0;
    overflow: hidden;
    background: var(--paper);
  }
  .poster {
    position: relative;
    width: 800px;
    height: 1200px;
    background: var(--paper);
    overflow: hidden;
  }
  .poster__field {
    position: absolute;
    left: 22px;
    top: 22px;
    width: 756px;
    height: 1156px;
    background: var(--mustard);
  }
  .poster__portrait {
    position: absolute;
    left: 190px;
    top: 126px;
  }
  .poster__title {
    position: absolute;
    left: 0;
    top: 0;
  }
  .title__line {
    font-family: "Michroma", sans-serif;
    text-transform: lowercase;
  }
  .title__line--upper { fill: var(--bone); }
  .title__line--lower { fill: var(--copper); }
  .poster__credits {
    position: absolute;
    left: 92px;
    top: 1070px;
    width: 572px;
    margin: 0;
    font-family: "Pathway Gothic One", sans-serif;
    font-size: 12.5px;
    line-height: 15.5px;
    text-align: center;
    text-transform: uppercase;
    color: var(--credit-ink);
  }
  .credits__minor { font-size: 7.5px; }
</style>
</head>
<body>
<div class="poster">
  <div class="poster__field">
    <svg class="poster__portrait" width="384" height="582" viewBox="0 0 384 582" role="img" aria-label="Stylised portrait of a bearded man, split into a dark brown half and a copper half">
      <defs>
        <linearGradient id="portraitTone" x1="0" y1="0" x2="1" y2="0">
          <stop offset="0" stop-color="var(--umber)"/>
          <stop offset="0.5" stop-color="#8a4d1c"/>
          <stop offset="1" stop-color="var(--rust)"/>
        </linearGradient>
      </defs>
      <path d="M192 0 C290 0 380 150 384 330 C386 480 300 582 192 582 C84 582 -2 480 0 330 C4 150 94 0 192 0 Z" fill="url(#portraitTone)"/>
    </svg>

    <svg class="poster__title" width="756" height="1156" viewBox="0 0 756 1156">
      <text class="title__line title__line--upper" x="58" y="890" font-size="92" textLength="640" lengthAdjust="spacingAndGlyphs">copper</text>
      <text class="title__line title__line--lower" x="58" y="997" font-size="104" textLength="640" lengthAdjust="spacingAndGlyphs">horizons</text>
    </svg>

    <p class="poster__credits">
      <span class="credits__minor">Lorem</span> ipsum dolor sit amet consectetur adipiscing elit <span class="credits__minor">sed vitae mi</span> vitae purus suscipit gravida integer aliquet <span class="credits__minor">turpis vitae</span>
      <span class="credits__minor">nulla pharetra</span> vehicula proin venenatis ut mi ut egestas pellentesque semper <span class="credits__minor">hendrerit tellus</span> ut aliquam justo fringilla sit
      amet quisque rutrum nul <span class="credits__minor">la sit amet enim egestas</span> vitae cursus nisi tempus aenean eu tempus ante <span class="credits__minor">nullam consequat</span> nibh in odio
      faucibus sollicitudin mauris vitae odio nisl
    </p>
  </div>
</div>
</body>
</html>
```